Lantern Vigor
Basketball Fitness Training
Lantern Vigor -
Creative Brief
Modern
Doran Fisk
Health and Fitness Coach
tavmirlo@quillpost.example
www.lanternvigor.example
Youth Development Clinics Private 1 on 1 Sessions Executive Training Women's Fitness Cross Training

```html
<!DOCTYPE html>
<html lang="en">
<head>
<meta charset="utf-8">
<title>Lantern Vigor – Business Card</title>
<link rel="stylesheet" href="https://fonts.googleapis.com/css2?family=Archivo+Black&family=Cambo&family=Open+Sans:wght@400;600&display=swap">
<style>
  :root {
    --page: #e9e6e1;
    --card: #ffffff;
    --ink: #141414;
    --navy: #1c3f94;
    --orange: #e8531a;
    --grey: #5a5f69;
  }
  * { margin: 0; padding: 0; box-sizing: border-box; }
  html, body {
    width: 1200px; height: 780px; overflow: hidden;
    background: var(--page);
  }
  .card {
    position: absolute; left: 40px; top: 40px;
    width: 1120px; height: 700px;
    background: var(--card);
    border-radius: 36px;
    overflow: hidden;
    box-shadow: 0 6px 24px rgba(0,0,0,.12);
  }
  .card__swoosh { position: absolute; inset: 0; width: 100%; height: 100%; }
  .brand {
    position: absolute; left: 80px; top: 70px;
    display: flex; align-items: center; gap: 22px;
  }
  .brand__dot {
    width: 64px; height: 64px; border-radius: 50%;
    background: var(--orange);
  }
  .brand__name {
    font-family: "Archivo Black", sans-serif;
    font-size: 74px; line-height: 1; color: var(--ink);
    letter-spacing: -1px;
  }
  .brand__tagline {
    position: absolute; left: 166px; top: 158px;
    font-family: "Archivo Black", sans-serif;
    font-size: 26px; color: var(--ink);
  }
  .person {
    position: absolute; left: 540px; top: 330px;
    width: 300px; text-align: center;
  }
  .person__name {
    font-family: "Cambo", serif;
    font-size: 48px; color: var(--navy); font-weight: 400;
  }
  .person__role {
    margin-top: 22px;
    font-family: "Open Sans", sans-serif;
    font-size: 23px; color: var(--orange);
  }
  .contact {
    position: absolute; left: 70px; top: 560px;
    list-style: none;
    font-family: "Open Sans", sans-serif;
    font-size: 21px; color: var(--grey);
  }
  .contact__item { display: flex; align-items: center; gap: 16px; margin-bottom: 14px; }
  .contact__icon { width: 22px; height: 22px; flex: none; }
</style>
</head>
<body>
  <article class="card">
    <svg class="card__swoosh" viewBox="0 0 1120 700" aria-hidden="true">
      <path d="M880 0 H1120 V700 H905 C1015 520 1015 230 880 0 Z" fill="var(--navy)"/>
      <path d="M730 700 C900 560 985 390 990 230 C1015 420 965 590 905 700 Z" fill="var(--orange)"/>
    </svg>

    <div class="brand">
      <span class="brand__dot"></span>
      <h1 class="brand__name">Lantern Vigor</h1>
    </div>
    <p class="brand__tagline">Basketball Fitness Training</p>

    <div class="person">
      <h2 class="person__name">Doran Fisk</h2>
      <p class="person__role">Health and Fitness Coach</p>
    </div>

    <ul class="contact">
      <li class="contact__item">
        <svg class="contact__icon" viewBox="0 0 24 24" aria-hidden="true">
          <circle cx="12" cy="12" r="10" fill="none" stroke="var(--navy)" stroke-width="2.4"/>
          <circle cx="12" cy="12" r="4" fill="none" stroke="var(--navy)" stroke-width="2.4"/>
        </svg>
        <span>tavmirlo@quillpost.example</span>
      </li>
      <li class="contact__item">
        <svg class="contact__icon" viewBox="0 0 24 24" aria-hidden="true">
          <g fill="none" stroke="var(--navy)" stroke-width="2">
            <circle cx="12" cy="12" r="10"/>
            <ellipse cx="12" cy="12" rx="4.5" ry="10"/>
            <path d="M2 12 H22 M4 7 H20 M4 17 H20"/>
          </g>
        </svg>
        <span>www.lanternvigor.example</span>
      </li>
    </ul>
  </article>
</body>
</html>
```